Velvet Brow Haven - Semi Permanent Makeup

Website Brief
Overview:
• Product - Cosmetics Tattooing \ Permanent Makeup
• Permanent beauty services including permanent eyebrow hairstrokes, eyeliner, lip liner, Lip Blend
• Marketing - over 18 year old women
• Website pages: Home – Services - About Renata – Pricing – Contact Us – Pre Procedures - Post Procedures (please read below for page titles in purple)
• There is logo and design all be done by pixel harbour and should be on file
Home Page
Pictures:
Logo: as per attachment
Slogan:
Special Offers:
Facebook: Setup and link on web page
Testimonials: What people are saying, Commits from clients
Marking box\Banner: that flicks around with either special offices, testimonials, location of Renata, slogans etc..
Services
Semi - Permanent Makeup
Eyebrows:
o Summary
o Before, After and healed pictures
Upper and Lower Eyeliner
o Summary
Lip Liner:
o Summary

Lip Blend:
o Summary
Corrections:
o Summary
Tattoo Removal:
o Summary

About Renata:
o Summary

Renata Studied Certificate:
QRTMVLA817C – Design and perform cosmetic tattooing
PKWOR615D – Maintain infection control standards in office practice setting
PKWCAR118 – Provide First Aid
Business Management - Frontline Management
Graduate Diploma - Project Management
Pricing:
Price List
Semi - Permanent Eyebrow Hairstrokes $430.00
Permanent Upper Eyeliner $420.00
Permanent Lower Eyeliner $420.00
Upper & Lower Eyeliner together $580.00
Lip Liner $360.00
Lip Blend $450.00
Tattoo Removal session $199.00
Consultation Free
• A follow-up appointment is included in all services within 4 to 6 weeks.

Aftercare Procedures Procedures:
o Summary
Contact Us:
Subscribe to mailing list:
o Email address
Contact Velvet Brow Haven:
• Name
• Phone
• Email address
• Preferred Contact Method
• Subscribe to newsletter , special offers and events
Location:
• By email: velvetbrowhaven@mailbrook.example
• By Phone:
o 0219374620
• Facebook: Velvet Brow Haven
• Address: 47 Fernhollow Street, Tarvel Cove, 8093, Christchurch
Updates

Project Deadline Extended
Reason: I have extended the dead line as I have been working 7days a week and given that some of the communication is restricted to due to time difference. I need extra time. Thanks to all design I will be back to shortly.

Target Market(s)

Over 18 years, all ages main females, but I do get a small amount of men

Industry/Entity Type

Tattoo

Coding

Coded - Design and coding required

Number of Pages Required

5+ page

Font styles to use
Sans Serif

Requirements
Must have
• Home page
• Services page
• About Renata page
• Pricing – Contact Us page
• Pre Procedures - Post care procedures page
• I would client to be able to subscribe to new letter
• Please go to my facebook page - Velvet Brow Haven - Christchurch, as the banner I have here, I would like to see on my webpage
Nice to have
• Please go on to my Facebook page as there client picture that could be used Velvet Brow Haven
• Before and after pictures
• Eyeliner
• Lip Liner
• Lip Blend
• Eyebrow Hair stroke
• The first two site below are my direct competitors, so I wold like something that is better that these:
• New Zealand:
• http://www.dawnpetalstudio.example.nz/
• http://www.glowlinebeauty.example.nz/

```html
<!DOCTYPE html>
<html lang="en">
<head>
<meta charset="utf-8">
<title>Velvet Brow Haven – Semi Permanent Makeup</title>
<link href="https://fonts.googleapis.com/css2?family=Lobster&family=Open+Sans:wght@400;600;700&display=swap" rel="stylesheet">
<style>
:root{
  --blue:#3a8fcf;
  --blue-deep:#2b7bbf;
  --blue-bright:#35a6df;
  --ink:#3b3b3b;
  --muted:#6b6b6b;
  --panel-dark:#464646;
  --btn-dark:#3a3a3a;
  --grey-bg:#ececec;
  --white:#ffffff;
}
*{box-sizing:border-box;margin:0;padding:0}
html,body{width:1200px;height:2517px;overflow:hidden;background:var(--white)}
body{position:relative;font-family:"Open Sans",Arial,sans-serif;color:var(--ink)}
.abs{position:absolute}

/* header */
.site-header{left:0;top:0;width:1200px;height:143px;background:linear-gradient(#ffffff,#f1f1f1)}
.top-contact{left:89px;top:25px;font-size:14px;color:#444;display:flex;align-items:center;gap:8px;white-space:nowrap}
.top-contact svg{width:15px;height:15px}
.header-rule{height:1px;background:#d6d6d6;top:72px}
.main-nav a{position:absolute;top:90px;font-family:"Lobster",cursive;font-size:17px;color:#444;text-decoration:none;transform:translateX(-50%);white-space:nowrap}
.main-nav a.active{color:var(--blue-deep)}
.brand{left:500px;top:38px;width:200px;text-align:center}
.brand-mark{width:34px;height:34px;border-radius:50%;background:var(--blue-deep);margin:0 auto 8px}
.brand-name{font-size:15px;font-weight:600;color:#333}
.social-dot{width:28px;height:28px;border-radius:50%;background:#dfe6f3;border:2px solid #c5cfe2}

/* hero */
.hero{left:0;top:143px;width:1200px;height:587px}
.hero-title{left:89px;font-size:36px;font-weight:600;color:#222;white-space:nowrap}
.hero-slogan{left:89px;font-size:20px;font-weight:600;color:#222}
.btn-appointment{left:89px;width:218px;height:50px;border-radius:6px;background:linear-gradient(#5a5a5a,#2f2f2f);color:#fff;font-size:16px;font-weight:600;display:flex;align-items:center;justify-content:center}
.slider-arrow{width:34px;height:34px;border-radius:50%;background:rgba(90,90,90,.75);border:2px solid rgba(255,255,255,.5)}
.hero-offer{right:33px;color:#fff;text-align:right}
.hero-offer h2{font-size:25px;font-weight:700}
.hero-offer .sub{font-size:19px;margin-top:2px}
.offer-list{position:absolute;left:835px;list-style:none;color:#fff;font-size:20px}
.offer-list li{display:flex;align-items:center;gap:14px;height:31px}
.offer-list svg{width:22px;height:20px}
.hero-contact{right:20px;color:#fff;font-size:18px;text-align:right;line-height:32px;white-space:nowrap}
.hero-contact .phone{font-size:20px}
.hero-contact b{color:var(--blue-bright);font-weight:700}

/* services */
.services{left:0;top:730px;width:1200px;height:482px;background:linear-gradient(var(--blue),#3b93d2 60%,#4a9ad6)}
.section-title{font-family:"Lobster",cursive;font-weight:400;font-size:31px;color:#fff;text-align:center;width:1200px;left:0}
.service{width:240px;text-align:center;color:#fff}
.service .thumb{width:168px;height:168px;border-radius:50%;border:4px solid #fff;margin:0 auto}
.service h3{font-family:"Lobster",cursive;font-weight:400;font-size:20px;margin-top:16px}
.service p{font-size:11px;line-height:18px;margin:10px auto 0;width:224px;text-align:justify}
.btn-outline{display:inline-block;margin-top:20px;width:86px;height:30px;border:1px solid #fff;border-radius:3px;font-size:10px;line-height:28px;color:#fff}

/* beauty spots */
.feature-band{left:0;top:1212px;width:1200px;height:315px;background:linear-gradient(135deg,#f3f3f3,#e2e2e2 50%,#f1f1f1)}
.feature{left:84px;top:1268px;width:1025px;height:204px;background:linear-gradient(var(--blue-deep),#2f7fb6);box-shadow:0 18px 22px -14px rgba(0,0,0,.45)}
.feature-photo{left:0;top:0;width:335px;height:204px;background:linear-gradient(120deg,#6a6f78,#b9b0ac 55%,#efe9e6)}
.feature-body{left:360px;top:22px;width:650px;color:#fff}
.feature-body h3{font-family:"Lobster",cursive;font-weight:400;font-size:26px}
.feature-body p{font-size:12.5px;line-height:20px;margin-top:8px}
.feature-body .more{font-size:13px;margin-top:10px}

/* booking */
.booking-title{left:84px;top:1567px;font-family:"Lobster",cursive;font-weight:400;font-size:29px;color:var(--blue-bright)}
.book-box{left:84px;top:1619px;width:592px;height:304px;background:var(--panel-dark)}
.book-head{height:54px;border-bottom:2px solid #5c5c5c;text-align:center;font-family:"Lobster",cursive;font-size:20px;color:#fff;line-height:52px}
.field{position:absolute;height:37px;background:#fff;border:1px solid #ccc;font-size:13px;color:#444;padding-left:11px;line-height:35px}
.btn-book{left:30px;top:257px;width:103px;height:29px;background:var(--blue-bright);color:#fff;font-size:11px;line-height:29px;text-align:center}
.news-box{left:696px;top:1616px;width:415px;height:309px;background:var(--blue-bright);border:4px solid #2a95cf;box-shadow:0 3px 6px rgba(0,0,0,.25)}
.news-box h3{position:absolute;left:37px;top:30px;font-family:"Lobster",cursive;font-weight:400;font-size:25px;color:#fff}
.news-box p{position:absolute;left:37px;top:76px;width:340px;font-size:13.5px;font-weight:600;line-height:21px;color:#fff;text-align:justify}
.news-box .field{font-size:10px;border-color:#1e7fb5}
.btn-subscribe{left:37px;top:237px;width:132px;height:37px;background:var(--btn-dark);color:#fff;font-size:15px;line-height:37px;text-align:center;border-radius:2px}

/* testimonials */
.testi-title{left:0;width:1200px;top:2015px;text-align:center;font-family:"Lobster",cursive;font-weight:400;font-size:29px;color:var(--blue-deep)}
.avatar{width:94px;height:94px;border-radius:50%;background:radial-gradient(#f2ddd0,#d7c3b5 70%,#ececec);border:3px solid #f3f3f3}
.quote{width:300px;font-size:12px;line-height:22px;color:#555}
.quote .mark{position:absolute;font-size:34px;color:#999;font-family:Georgia,serif;line-height:1}
.client-name{font-size:11px;font-weight:700;color:var(--blue-deep);margin-top:8px}
.client-role{font-size:12px;color:#555;margin-top:4px}
.testi-arrow{width:24px;height:40px}

/* footer */
.site-footer{left:0;top:2295px;width:1200px;height:160px;background:var(--blue)}
.footer-bottom{left:0;top:2455px;width:1200px;height:62px;background:#3387c9;border-top:1px solid #5aa0d6;text-align:center;color:#fff;font-size:12px;line-height:60px}
.foot-h{font-family:"Lobster",cursive;font-size:19px;color:#fff}
.foot-label{font-size:12px;color:#fff}
.foot-val{font-size:15px;color:#fff;display:flex;align-items:center;gap:12px;white-space:nowrap}
.foot-val svg{width:18px;height:18px}
.foot-small{font-size:12px;line-height:20px;color:#fff}
.social-square{width:34px;height:34px;background:#f2f2f2;border-radius:3px}
</style>
</head>
<body>

<header class="abs site-header">
  <div class="abs top-contact">
    <svg viewBox="0 0 16 16"><rect width="16" height="16" rx="3" fill="#3a8fcf"/><path d="M5 3.5l1.8 2.2-1 1.1a6 6 0 0 0 3.4 3.4l1.1-1 2.2 1.8-.9 1.5C8 12.6 3.4 8 3.5 4.4z" fill="#fff"/></svg>
    <span>+64 219374620</span>
    <span style="margin:0 6px">|</span>
    <svg viewBox="0 0 16 16"><rect width="16" height="16" rx="3" fill="#3a8fcf"/><path d="M3 5h10v6H3z" fill="none" stroke="#fff" stroke-width="1.2"/><path d="M3 5l5 4 5-4" fill="none" stroke="#fff" stroke-width="1.2"/></svg>
    <span>velvetbrowhaven@mailbrook.example</span>
  </div>
  <div class="abs header-rule" style="left:84px;width:399px"></div>
  <div class="abs header-rule" style="left:716px;width:397px"></div>
  <nav class="main-nav">
    <a class="active" style="left:104px">Home</a>
    <a style="left:196px">Services</a>
    <a style="left:319px">About Renata</a>
    <a style="left:437px">Pricing</a>
    <a style="left:741px">Gallery</a>
    <a style="left:861px">Call procedure</a>
    <a style="left:974px">FAQ's</a>
    <a style="left:1077px">Contact Us</a>
  </nav>
  <div class="abs brand">
    <div class="brand-mark"></div>
    <div class="brand-name">Velvet Brow Haven</div>
  </div>
  <div class="abs social-dot" style="left:1080px;top:21px" aria-hidden="true"></div>
</header>

<section class="abs hero">
  <svg width="1200" height="587" viewBox="0 0 1200 587" style="position:absolute;left:0;top:0">
    <defs>
      <linearGradient id="heroTone" x1="0" x2="1" y1="0" y2="0">
        <stop offset="0" stop-color="#8a8a58"/>
        <stop offset=".25" stop-color="#cfc39f"/>
        <stop offset=".45" stop-color="#e9c9b3"/>
        <stop offset=".62" stop-color="#d9ae96"/>
        <stop offset=".68" stop-color="#3a2b24"/>
        <stop offset="1" stop-color="#2a221d"/>
      </linearGradient>
    </defs>
    <rect width="1200" height="587" fill="url(#heroTone)" role="img" aria-label="Portrait photograph of a woman with blue eyes and permanent makeup"/>
    <path d="M0 455 Q560 650 1200 455 L1200 587 L0 587Z" fill="#3a8fcf"/>
  </svg>
  <div class="abs hero-title" style="top:209px">Velvet Brow Haven</div>
  <div class="abs hero-slogan" style="top:275px">Achieve Your Ideal Appearance</div>
  <div class="abs btn-appointment" style="top:339px">MAKE APPOINTMENT</div>
  <svg class="abs slider-arrow" style="left:92px;top:430px" viewBox="0 0 34 34"><path d="M19 11l-6 6 6 6" fill="none" stroke="#fff" stroke-width="2.5"/></svg>
  <svg class="abs slider-arrow" style="left:136px;top:430px" viewBox="0 0 34 34"><path d="M15 11l6 6-6 6" fill="none" stroke="#fff" stroke-width="2.5"/></svg>
  <div class="abs hero-offer" style="top:87px">
    <h2>Quality Services by Renata</h2>
    <div class="sub">Cosmetic Tattoo / Permanent Makeup</div>
  </div>
  <ul class="offer-list" style="top:162px">
    <li><svg viewBox="0 0 22 20"><path d="M2 11l6 6L20 3" fill="none" stroke="#3fa9e6" stroke-width="4"/></svg>Eyebrows</li>
    <li><svg viewBox="0 0 22 20"><path d="M2 11l6 6L20 3" fill="none" stroke="#3fa9e6" stroke-width="4"/></svg>Upper Eyeliner</li>
    <li><svg viewBox="0 0 22 20"><path d="M2 11l6 6L20 3" fill="none" stroke="#3fa9e6" stroke-width="4"/></svg>Lower Eyeliner</li>
    <li><svg viewBox="0 0 22 20"><path d="M2 11l6 6L20 3" fill="none" stroke="#3fa9e6" stroke-width="4"/></svg>Lip Liner</li>
    <li><svg viewBox="0 0 22 20"><path d="M2 11l6 6L20 3" fill="none" stroke="#3fa9e6" stroke-width="4"/></svg>Lip Blend</li>
  </ul>
  <div class="abs hero-contact" style="top:345px">
    <div class="phone"><b>phone:</b> 0219374620</div>
    <div><b>email:</b> velvetbrowhaven@mailbrook.example</div>
  </div>
</section>

<section class="abs services">
  <h2 class="abs section-title" style="top:35px">Our Services</h2>
  <div class="abs service" style="left:83px;top:111px">
    <div class="thumb" role="img" aria-label="Photo of an eyebrow treatment" style="background:linear-gradient(135deg,#c45a3a,#e9c8b6)"></div>
    <h3>Eyebrow</h3>
    <p>Lorem Ipsum has been the industry's standard dummy text ever since the 1500s, when an unknown printer took a galley</p>
    <span class="btn-outline">Read More »</span>
  </div>
  <div class="abs service" style="left:345px;top:111px">
    <div class="thumb" role="img" aria-label="Photo of an eyeliner treatment" style="background:linear-gradient(135deg,#e3c2ad,#b88670)"></div>
    <h3>Eyeliner</h3>
    <p>Lorem Ipsum has been the industry's standard dummy text ever since the 1500s, when an unknown printer took a galley</p>
    <span class="btn-outline">Read More »</span>
  </div>
  <div class="abs service" style="left:612px;top:111px">
    <div class="thumb" role="img" aria-label="Photo of a lip liner treatment" style="background:linear-gradient(135deg,#f2e5e0,#d99aa0)"></div>
    <h3>Lip liner &amp; Lip blend</h3>
    <p>Lorem Ipsum has been the industry's standard dummy text ever since the 1500s, when an unknown printer took a galley</p>
    <span class="btn-outline">Read More »</span>
  </div>
  <div class="abs service" style="left:873px;top:111px">
    <div class="thumb" role="img" aria-label="Photo of a tattoo removal result" style="background:linear-gradient(135deg,#9e7a5f,#d8b29a)"></div>
    <h3>Tattoo removal</h3>
    <p>Lorem Ipsum has been the industry's standard dummy text ever since the 1500s, when an unknown printer took a galley</p>
    <span class="btn-outline">Read More »</span>
  </div>
</section>

<section class="abs feature-band"></section>
<article class="abs feature">
  <div class="abs feature-photo" role="img" aria-label="Photo of a client receiving a cosmetic tattoo treatment"></div>
  <div class="abs feature-body">
    <h3>Beauty spots</h3>
    <p>Lorem Ipsum has been the industry's standard dummy text ever since the 1500s, when an unknown printer took a galley of type and scrambled it to make a type specimen book. It has survived not only five centuries, but also the leap into electronic typesetting, remaining essentially unchanged. It was popularised in the 1960s with the release of Letraset sheets containing Lorem Ipsum passages, and more recently</p>
    <div class="more">Read More »</div>
  </div>
</article>

<h2 class="abs booking-title">Booking</h2>
<form class="abs book-box">
  <div class="book-head">Book Now</div>
  <div class="field" style="left:30px;top:69px;width:254px">First Name</div>
  <div class="field" style="left:304px;top:69px;width:253px">Last Name</div>
  <div class="field" style="left:30px;top:116px;width:254px">Phone</div>
  <div class="field" style="left:304px;top:116px;width:253px">Email id</div>
  <div class="field" style="left:30px;top:162px;width:254px">Service
    <svg style="position:absolute;right:10px;top:15px" width="8" height="5" viewBox="0 0 8 5"><path d="M0 0h8L4 5z" fill="#444"/></svg></div>
  <div class="field" style="left:304px;top:162px;width:253px">Date
    <svg style="position:absolute;right:9px;top:12px" width="11" height="11" viewBox="0 0 11 11"><rect x=".5" y="1.5" width="10" height="9" fill="none" stroke="#555"/><path d="M.5 4h10M3 6h1M6 6h1M3 8h1M6 8h1" stroke="#555"/></svg></div>
  <div class="field" style="left:30px;top:208px;width:527px">Message</div>
  <div class="abs btn-book">BOOK NOW</div>
</form>

<aside class="abs news-box">
  <h3>Newsletter Subscribers</h3>
  <p>Excepteur sint occaecat cupidatat non proident, sunt in culpa qui officia deserunt mollit anim</p>
  <div class="field" style="left:37px;top:137px;width:335px">Name</div>
  <div class="field" style="left:37px;top:186px;width:335px">Enter your email address</div>
  <div class="abs btn-subscribe">Subscribers</div>
</aside>

<h2 class="abs testi-title">Testimonials</h2>
<svg class="abs testi-arrow" style="left:62px;top:2128px" viewBox="0 0 24 40"><path d="M20 2L4 20l16 18" fill="none" stroke="#aaa" stroke-width="2"/></svg>
<svg class="abs testi-arrow" style="left:1112px;top:2128px" viewBox="0 0 24 40"><path d="M4 2l16 18L4 38" fill="none" stroke="#aaa" stroke-width="2"/></svg>

<div class="abs avatar" style="left:107px;top:2090px" role="img" aria-label="Client photo"></div>
<div class="abs quote" style="left:238px;top:2100px">
  <span class="mark" style="left:-16px;top:-6px">“</span>
  Highly recommend getting your eyebrows done. At 70 year old I had concerns about experiencing pain. I felt none and love my results.
  <span class="mark" style="left:260px;top:70px">”</span>
  <div class="client-name">MARA ELLISON</div>
  <div class="client-role">Marketing Executive</div>
</div>

<div class="abs avatar" style="left:655px;top:2090px" role="img" aria-label="Client photo"></div>
<div class="abs quote" style="left:792px;top:2100px">
  <span class="mark" style="left:-18px;top:-6px">“</span>
  I can't express how happy I am with the result of my eyebrows! I was so nervous but am so pleased with the result. My eyebrows look so natural
  <span class="mark" style="left:205px;top:70px">”</span>
  <div class="client-name">TESSA QUINLAN</div>
  <div class="client-role">Marketing Executive</div>
</div>

<footer class="abs site-footer">
  <div class="abs foot-h" style="left:86px;top:33px">Contacts</div>
  <div class="abs foot-label" style="left:86px;top:70px">Address</div>
  <div class="abs foot-small" style="left:86px;top:95px;width:190px">47 Fernhollow Street, Tarvel Cove 8093, Christchurch</div>
  <div class="abs foot-label" style="left:309px;top:78px">Phone Number</div>
  <div class="abs foot-val" style="left:303px;top:104px">
    <svg viewBox="0 0 18 18"><path d="M4 2l3 3.5-1.5 1.7a9 9 0 0 0 5.3 5.3L12.5 11 16 14l-1.5 2.2C8 16 2 10 1.8 3.5z" fill="none" stroke="#fff" stroke-width="1.3"/></svg>+64 219374620</div>
  <div class="abs foot-label" style="left:515px;top:78px">Email id</div>
  <div class="abs foot-val" style="left:515px;top:104px">
    <svg viewBox="0 0 18 18"><rect x="1.5" y="4" width="15" height="10" fill="none" stroke="#fff" stroke-width="1.3"/><path d="M1.5 4L9 10l7.5-6" fill="none" stroke="#fff" stroke-width="1.3"/></svg>velvetbrowhaven@mailbrook.example</div>
  <div class="abs foot-h" style="left:970px;top:33px">Social Media</div>
  <div class="abs social-square" style="left:970px;top:78px" aria-hidden="true"></div>
</footer>
<div class="abs footer-bottom">2016&nbsp; All Rights Reserved.</div>

</body>
</html>
```